Meridel Haulage - Website

A clean, not cluttered informative website for our business. We specialize in the transportation of radioactive materials across North America. The site is mostly for information about our company and will not be used to attract business but will be used to attract employee's mainly drivers. Driver's are very hard to find in our area. One of the pages needs to be a job's posting page with an apply now button. Either an application can be filled out there or a resume can be uploaded which ever functionality works better. I would like a website that I can easily edit, ability to change text and photos.

Number of Pages Required

5+ page

Colors

Designer to choose colors to be used in the design.

Requirements
Must have
• Home - About - Services - Jobs - Contact pages
• A way prospective employee's can apply or upload their resume to be emailed to me
• Very clean apperance
Should not have
• I don't want it to be busy

```html
<!DOCTYPE html>
<html lang="en">
<head>
<meta charset="utf-8">
<title>Meridel Haulage</title>
<link href="https://fonts.googleapis.com/css2?family=Poppins:wght@400;500&family=Roboto:wght@500;700&display=swap" rel="stylesheet">
<style>
:root{
  --blue:#1572be;
  --blue-deep:#0f5fa3;
  --grey:#6d6e71;
  --text:#333333;
  --footer:#1b72ba;
  --bar:#7b7c7e;
  --white:#ffffff;
  --line:#e6e6e6;
}
*{box-sizing:border-box;margin:0;padding:0}
html,body{width:1200px;height:2525px;overflow:hidden}
body{position:relative;background:var(--white);font-family:"Poppins",sans-serif;color:var(--text)}
.abs{position:absolute}

/* header */
.brand{left:81px;top:50px;font-family:"Roboto",sans-serif;font-weight:700;font-size:38px;color:var(--blue);letter-spacing:1px;display:flex;align-items:center;gap:12px}
.brand-dot{width:16px;height:16px;border-radius:50%;background:var(--blue)}
.topline{top:22px;right:82px;display:flex;align-items:center;gap:22px;font-size:16px;color:#333}
.topline span{display:flex;align-items:center;gap:8px}
.topline .phone{font-size:19px}
.nav{top:76px;right:82px;display:flex;gap:42px;font-size:18px;color:var(--blue-deep)}
.nav a{color:inherit;text-decoration:none}

/* hero */
.hero{left:0;top:126px;width:1200px;height:493px;background:linear-gradient(180deg,#c9ccd0 0%,#a9a7a4 35%,#6e6c6b 62%,#7a7a72 78%,#5d5f56 100%)}
.hero-arrow{top:340px;width:38px;height:36px;background:rgba(40,40,40,.75);display:flex;align-items:center;justify-content:center}
.hero-title{left:0;top:515px;width:1200px;text-align:center;color:var(--white);font-weight:500;font-size:39px;line-height:50px;text-shadow:0 2px 4px rgba(0,0,0,.7)}

/* sections */
.heading{left:0;width:1200px;text-align:center;font-family:"Roboto",sans-serif;font-weight:500;font-size:40px;color:var(--blue)}
.heading .muted{color:var(--grey)}
.rule{left:525px;width:150px;height:2px;background:#9a9a9a}
.subhead{left:0;top:754px;width:1200px;text-align:center;font-size:20px;color:var(--blue);font-weight:500}
.lead{left:112px;width:976px;text-align:center;font-size:16px;line-height:29px;color:#333}
.btn{background:var(--blue);color:var(--white);font-size:19px;display:flex;align-items:center;justify-content:center;box-shadow:3px 4px 5px rgba(0,0,0,.35)}
.divider{left:96px;width:1008px;height:2px;background:linear-gradient(90deg,transparent,var(--line),transparent)}

/* service cards */
.card{top:1210px;width:241px}
.card-photo{width:241px;height:205px;border:2px solid var(--blue);padding:5px;background:var(--white)}
.card-photo div{width:100%;height:100%}
.card-title{margin-top:22px;text-align:center;font-family:"Roboto",sans-serif;font-weight:500;font-size:19px;line-height:27px;color:#222}
.card-text{margin-top:10px;text-align:center;font-size:14px;line-height:25.5px;color:#333}
.card .btn{width:135px;height:45px;margin:22px auto 0}

.apply{left:470px;top:1986px;width:257px;height:99px;background:var(--blue);color:var(--white);text-align:center;font-family:"Roboto",sans-serif;font-weight:700;box-shadow:3px 4px 6px rgba(0,0,0,.35);display:flex;flex-direction:column;justify-content:center;border:1px solid #0d5a9c}
.apply .a1{font-size:22px}
.apply .a2{font-size:20px}

/* footer */
.footer{left:0;top:2163px;width:1200px;height:314px;background:var(--footer);color:var(--white)}
.f-title{font-family:"Roboto",sans-serif;font-weight:500;font-size:18px;top:35px}
.f-rule{top:70px;width:46px;height:2px;background:var(--white)}
.f-links{left:84px;top:96px;list-style:none;font-size:15px;line-height:36px}
.f-item{display:flex;align-items:flex-start;gap:14px;font-size:15px;line-height:25px;left:242px}
.map{left:572px;top:99px;width:285px;height:168px;background:linear-gradient(135deg,#e9ecef,#d9dee3 60%,#cfd8de)}
.social{top:101px;width:30px;height:30px;border-radius:50%;background:#8a8d90}
.apply-small{left:917px;top:143px;width:204px;height:79px;background:#6f7274;border:2px solid #9fa2a4;color:var(--white);text-align:center;font-family:"Roboto",sans-serif;font-weight:700;display:flex;flex-direction:column;justify-content:center;box-shadow:2px 3px 4px rgba(0,0,0,.3)}
.apply-small .a1{font-size:17px}
.apply-small .a2{font-size:15px}
.bar{left:0;top:2477px;width:1200px;height:48px;background:var(--bar);color:var(--white);font-size:14px}
.bar-copy{left:84px;top:13px}
.sq{top:7px;width:34px;height:34px}
</style>
</head>
<body>

<header>
  <div class="abs brand"><span class="brand-dot"></span>MERIDEL HAULAGE</div>
  <div class="abs topline">
    <span>
      <svg width="28" height="20" viewBox="0 0 28 20"><rect x="1" y="1" width="26" height="18" fill="none" stroke="#1572be" stroke-width="2"/><path d="M1 1 L14 11 L27 1" fill="none" stroke="#1572be" stroke-width="2"/></svg>
      inquiry@meridelhaulage.com
    </span>
    <span class="phone">
      <svg width="26" height="26" viewBox="0 0 24 24"><path d="M6.6 10.8a15.1 15.1 0 006.6 6.6l2.2-2.2c.3-.3.7-.4 1-.2 1.1.4 2.3.6 3.6.6.6 0 1 .4 1 1V20c0 .6-.4 1-1 1A17 17 0 013 4c0-.6.4-1 1-1h3.5c.6 0 1 .4 1 1 0 1.3.2 2.5.6 3.6.1.3 0 .7-.2 1z" fill="#1572be"/></svg>
      555.014.2290
    </span>
  </div>
  <nav class="abs nav">
    <a href="#">Home</a><a href="#">About Us</a><a href="#">Services</a><a href="#">Jobs</a><a href="#">Contact Us</a>
  </nav>
</header>

<section>
  <div class="abs hero" role="img" aria-label="Photo of a tractor-trailer hauling secured cylindrical containers in front of a brick building"></div>
  <div class="abs hero-arrow" style="left:0">
    <svg width="12" height="16" viewBox="0 0 12 16"><path d="M9 2 L3 8 L9 14" fill="none" stroke="#fff" stroke-width="2.5"/></svg>
  </div>
  <div class="abs hero-arrow" style="right:0">
    <svg width="12" height="16" viewBox="0 0 12 16"><path d="M3 2 L9 8 L3 14" fill="none" stroke="#fff" stroke-width="2.5"/></svg>
  </div>
  <h1 class="abs hero-title">We Specialize In The Transportation of Radioactive<br>Materials Across North America</h1>
</section>

<section>
  <h2 class="abs heading" style="top:678px">ABOUT MERIDEL <span class="muted">HAULAGE</span></h2>
  <div class="abs rule" style="top:732px"></div>
  <p class="abs subhead">We Serve Accross Whole North America</p>
  <p class="abs lead" style="top:788px">Lorem ipsum dolor sit amet, consectetuer adipiscing elit, sed diam nonummy nibh euismod tincidunt ut laoreet dolore magna aliquam erat volutpat. Ut wisi enim ad minim veniam, quis nostrud exerci tation ullamcorper suscipit lobortis nisl aliquip ex ea commodo consequat. Duis autem vel eum iriure dolor in hendrerit ivulputate velit esse molestie consequat, vel illum dolore eu feugiat nulla facilisis</p>
  <div class="abs btn" style="left:528px;top:919px;width:137px;height:49px">Read More</div>
  <div class="abs divider" style="top:1043px"></div>
</section>

<section>
  <h2 class="abs heading" style="top:1109px">OUR <span class="muted">SERVICES</span></h2>
  <div class="abs rule" style="top:1162px;left:557px;width:86px"></div>

  <article class="abs card" style="left:81px">
    <div class="card-photo"><div role="img" aria-label="Photo of a driver at the wheel inside a truck cab" style="background:linear-gradient(160deg,#8fa7a0,#4c5a58 55%,#2b3133)"></div></div>
    <h3 class="card-title">For<br>Experienced Drivers</h3>
    <p class="card-text">Lorem ipsum dolor sit amet, consectetuer adipiscing elit, sed diam nonummy nibh euismod tincidunt ut laoreet dolore magna aliquam erat volutpat.</p>
    <div class="btn">Read More</div>
  </article>

  <article class="abs card" style="left:347px">
    <div class="card-photo"><div role="img" aria-label="Photo of trainees using a truck driving simulator" style="background:linear-gradient(160deg,#c9c9c4,#6f7372 55%,#2d2f31)"></div></div>
    <h3 class="card-title">For<br>Inexperienced Drivers</h3>
    <p class="card-text">Lorem ipsum dolor sit amet, consectetuer adipiscing elit, sed diam nonummy nibh euismod tincidunt ut laoreet dolore magna aliquam erat volutpat.</p>
    <div class="btn">Read More</div>
  </article>

  <article class="abs card" style="left:613px">
    <div class="card-photo"><div role="img" aria-label="Photo of a smiling driver giving a thumbs up beside a blue truck" style="background:linear-gradient(160deg,#2f6fb0,#6f9cc8 50%,#8a8f96)"></div></div>
    <h3 class="card-title">For<br>CDL Training</h3>
    <p class="card-text">Lorem ipsum dolor sit amet, consectetuer adipiscing elit, sed diam nonummy nibh euismod tincidunt ut laoreet dolore magna aliquam erat volutpat.</p>
    <div class="btn">Read More</div>
  </article>

  <article class="abs card" style="left:878px">
    <div class="card-photo"><div role="img" aria-label="Photo of a veteran driver standing with arms crossed" style="background:linear-gradient(170deg,#e8e8e6,#c9c5c0 45%,#1f3e6b 75%)"></div></div>
    <h3 class="card-title">For<br>Military Veterans</h3>
    <p class="card-text">Lorem ipsum dolor sit amet, consectetuer adipiscing elit, sed diam nonummy nibh euismod tincidunt ut laoreet dolore magna aliquam erat volutpat.</p>
    <div class="btn">Read More</div>
  </article>

  <div class="abs divider" style="top:1764px"></div>
</section>

<section>
  <h2 class="abs heading" style="top:1833px">FOR INSTERESTED <span class="muted">TRUCK DRIVERS</span></h2>
  <div class="abs rule" style="top:1887px;left:548px;width:104px"></div>
  <p class="abs lead" style="top:1907px;left:90px;width:1020px">Lorem ipsum dolor sit amet, consectetuer adipiscing elit, sed diam nonummy nibh euismod tincidunt ut laoreet dolore magna aliquam erat volutpat. Ut wisi enim ad minim veniam, quis nostrud exerci ttation.</p>
  <div class="abs apply"><span class="a1">APPLY NOW</span><span class="a2">MH Driver Application</span></div>
</section>

<footer class="abs footer">
  <h4 class="abs f-title" style="left:84px">Quick Links</h4>
  <div class="abs f-rule" style="left:84px"></div>
  <ul class="abs f-links">
    <li>Home</li><li>About Us</li><li>Services</li><li>Jobs</li><li>Contact Us</li>
  </ul>

  <h4 class="abs f-title" style="left:242px">Contact Details</h4>
  <div class="abs f-rule" style="left:242px"></div>
  <div class="abs f-item" style="top:96px">
    <svg width="18" height="26" viewBox="0 0 18 26"><path d="M9 1a8 8 0 00-8 8c0 6 8 16 8 16s8-10 8-16a8 8 0 00-8-8z" fill="#fff"/><circle cx="9" cy="9" r="3" fill="#1b72ba"/></svg>
    <span>Street Name, City Name<br>State Zipcode</span>
  </div>
  <div class="abs f-item" style="top:163px">
    <svg width="22" height="22" viewBox="0 0 24 24"><circle cx="12" cy="12" r="11" fill="none" stroke="#fff" stroke-width="1.6"/><path d="M8 7.5c.5 3.5 4 8 8.5 8.5l1-1.6-2.3-1.3-1 1c-1.6-.6-3-2.1-3.6-3.6l1-1-1.3-2.3z" fill="#fff"/></svg>
    <span>555.014.2290</span>
  </div>
  <div class="abs f-item" style="top:222px">
    <svg width="22" height="16" viewBox="0 0 22 16"><rect x="1" y="1" width="20" height="14" fill="none" stroke="#fff" stroke-width="1.6"/><path d="M1 1 L11 9 L21 1" fill="none" stroke="#fff" stroke-width="1.6"/></svg>
    <span>inquiry@meridelhaulage.com</span>
  </div>

  <h4 class="abs f-title" style="left:572px">Location Map</h4>
  <div class="abs f-rule" style="left:572px"></div>
  <div class="abs map" role="img" aria-label="Street map showing the company location"></div>

  <h4 class="abs f-title" style="left:914px">Follow Us On</h4>
  <div class="abs f-rule" style="left:914px"></div>
  <div class="abs social" style="left:916px"></div>
  <div class="abs social" style="left:960px"></div>
  <div class="abs social" style="left:1004px"></div>
  <div class="abs apply-small"><span class="a1">APPLY NOW</span><span class="a2">MH Driver Application</span></div>
</footer>

<div class="abs bar">
  <p class="abs bar-copy">Copyright © 2019 Meridel Haulage. All Rights Reserved.</p>
  <div class="abs sq" style="left:958px;background:#3b5998"></div>
  <div class="abs sq" style="left:1002px;background:#3aa1d8"></div>
  <div class="abs sq" style="left:1046px;background:#0e6aa6"></div>
  <div class="abs sq" style="left:1086px;background:#d6322b"></div>
</div>

</body>
</html>
```